Gym opening flyer

We need a flyer design for the opening/launch of our gym. We need the flyer ASAP. So we would like to choose the flyer as soon as possible. We will open the gym on Saturday, Feb 10. The flyer should have a front and back side

We would like to base the flyer on the following flyer (see link below) or something similar.

https://lumiqo.example/images/RtkWbz

I have also uploaded/attached our logo and pictures that we would like to use in our flyer. I have also attached a drawings of the front and back side of the flyer of what changes I would like (compared to the flyer in the link above).

You can use the text for Abour Us, Facilities from our webside www.vordo.example

Target Market(s)

Dubai, UAE

Industry/Entity Type

Fitness

Font styles to use
Other font styles liked:
• Primal

Requirements
Must have
• We need the design ASAP. We must have the Logo on the flyer and that we are opening on Feb 10th and that we have an open house between 10am to 7pm. We also need references to
• our website www.vordo.example
• Instagram @vordofit
• Facebook @vordofit
• Special offer that the flyer entitles the person to 3 free classes that is valid for one month until March 10, 2018.
Nice to have
• see above
Should not have
• see above

```html
<!DOCTYPE html>
<html lang="en">
<head>
<meta charset="utf-8">
<title>Vordo Dubai – Grand Opening Flyer</title>
<link rel="stylesheet" href="https://fonts.googleapis.com/css2?family=Passion+One:wght@400;700&family=Russo+One&family=Rokkitt:ital,wght@0,500;0,700;1,700&family=Ubuntu:wght@400;500;700&family=Ubuntu+Condensed&display=swap">
<style>
:root{
  --yellow:#f6e31c;
  --ink:#111214;
  --slate:#4a4c4a;
  --slate-dark:#2e302f;
  --paper:#ffffff;
  --band:#e6e7e8;
  --navy:#1f3550;
  --condensed:"Ubuntu Condensed","Ubuntu","Arial Narrow",sans-serif;
}
*{box-sizing:border-box;margin:0;padding:0}
html,body{width:1200px;height:849px;overflow:hidden;background:var(--paper)}
.canvas{position:relative;width:1200px;height:849px;background:var(--paper);font-family:"Ubuntu",sans-serif}
.page{position:absolute;top:33px;width:540px;height:763px;overflow:hidden}
.front{left:50px;background:radial-gradient(ellipse at 40% 60%,#5a5c59,#3c3e3c 70%,#2f312f)}
.back{left:621px;background:#3b3d3a}

/* front header */
.header{position:absolute;left:0;top:0;width:540px;height:157px;background:linear-gradient(180deg,#3a3c3a,#4d4f4c)}
.header-strip{position:absolute;left:0;top:43px;width:540px;height:50px;background:var(--ink)}
.ages{position:absolute;left:10px;top:48px;color:#fff;font-size:11px;line-height:12px;transform:rotate(-14deg);text-align:center;white-space:nowrap}
.brand-left,.brand-right{position:absolute;top:47px;color:#fff;font-family:"Russo One",sans-serif;font-size:40px;letter-spacing:2px;line-height:42px;white-space:nowrap}
.brand-left{left:78px}
.brand-right{left:352px}
.brand-seal{position:absolute;left:251px;top:32px;width:90px;height:90px;border-radius:50%;background:var(--ink);border:3px solid #fff}
.rule-yellow{position:absolute;left:0;width:540px;height:4px;background:var(--yellow)}

.hero-photo{position:absolute;left:318px;top:243px;width:222px;height:520px;background:linear-gradient(180deg,#6b5a52 0%,#3a2e2b 35%,#1e1d1f 70%,#2b2c2e 100%);border-radius:90px 90px 0 0}

.title{position:absolute;left:18px;top:180px;font-family:"Passion One",sans-serif;font-weight:700;font-size:66px;line-height:70px;color:#fff;letter-spacing:1px;-webkit-text-stroke:1.5px #222;text-shadow:2px 3px 0 #222;white-space:nowrap}
.title-rule{position:absolute;left:16px;top:250px;width:384px;height:2px;background:#ddd}
.date{position:absolute;left:22px;top:258px;font-family:"Passion One",sans-serif;font-size:28px;line-height:32px;color:#fff;letter-spacing:1px;-webkit-text-stroke:1px #222;white-space:nowrap}
.date sup{font-size:16px}
.date-rule{position:absolute;left:16px;top:292px;width:384px;height:2px;background:#ddd}

.timetable-head{position:absolute;left:14px;top:307px;width:346px;height:38px;border:2px solid var(--yellow);color:var(--yellow);font-family:"Rokkitt",serif;font-style:italic;font-weight:700;font-size:21px;letter-spacing:1px;padding:4px 14px;white-space:nowrap}
.timeline{position:absolute;left:56px;top:345px;width:3px;height:148px;background:var(--yellow)}
.slot{position:absolute;left:56px;display:flex;align-items:center;font-family:"Rokkitt",serif;font-weight:500;font-size:17px;color:#fff;white-space:nowrap}
.slot::before{content:"";width:34px;height:3px;background:var(--yellow)}
.slot::after{content:"";position:absolute;left:32px;width:7px;height:7px;border-radius:50%;background:#fff}
.slot .time{width:70px;margin-left:10px}

.offer-band{position:absolute;left:0;top:527px;width:540px;height:46px;background:var(--yellow)}
.offer-label{position:absolute;left:0;top:515px;width:106px;height:58px;background:var(--ink);color:var(--yellow);font-family:"Passion One",sans-serif;font-size:27px;line-height:25px;padding:6px 8px;white-space:nowrap}
.offer-text{position:absolute;left:106px;top:517px;width:232px;height:56px;background:var(--yellow);border:1px solid var(--ink);color:var(--ink);font-size:12px;font-weight:700;line-height:15px;padding:4px 6px;text-align:justify}

.about-head{position:absolute;left:24px;top:586px;color:#fff;font-size:15px;font-weight:500;white-space:nowrap}
.about-head::before{content:"●●● ";font-size:8px;letter-spacing:-1px;color:#ccc;vertical-align:2px}
.about-text{position:absolute;left:24px;top:612px;width:274px;color:#fff;font-size:13px;line-height:17.6px;text-align:justify}
.call{position:absolute;left:24px;top:700px;font-family:"Passion One",sans-serif;font-size:38px;line-height:42px;color:var(--yellow);letter-spacing:1px;white-space:nowrap}

/* back */
.photo{position:absolute;top:0;height:163px}
.scene{position:absolute;left:0;top:166px;width:540px;height:440px;background:linear-gradient(90deg,#3a3d3a 0%,#4b4d47 40%,#8d8170 75%,#c9a883 100%)}
.facilities-head{position:absolute;left:46px;top:183px;font-family:"Passion One",sans-serif;font-size:30px;line-height:34px;color:#fff;-webkit-text-stroke:1px #111;white-space:nowrap}
.pill{position:absolute;left:31px;width:198px;height:27px;border-radius:14px;background:var(--yellow);color:var(--ink);font-family:var(--condensed);font-size:19px;text-align:center;line-height:28px;white-space:nowrap;overflow:hidden}
.desc{position:absolute;left:17px;width:241px;color:var(--yellow);font-size:11.5px;line-height:15px;text-align:justify}
.follow{position:absolute;left:17px;top:581px;color:#fff;font-family:var(--condensed);font-size:20px;line-height:24px;white-space:nowrap}
.social{position:absolute;top:607px;height:50px;background:#e2e2e2;display:flex;align-items:center;padding-left:12px;gap:9px;font-family:var(--condensed);font-size:20px;white-space:nowrap}
.social .mark{width:28px;height:28px;flex:none}
.social-a{left:9px;width:153px;color:var(--navy)}
.social-a .mark{background:var(--navy)}
.social-b{left:169px;width:157px;color:#9b2f86}
.social-b .mark{background:#9b2f86}
.info-band{position:absolute;left:0;top:673px;width:540px;height:75px;background:var(--band);text-align:center;color:var(--slate-dark)}
.info-links{font-family:var(--condensed);font-size:25px;line-height:32px;letter-spacing:1px;margin-top:8px;white-space:nowrap}
.info-site{font-size:13px;line-height:30px;white-space:nowrap}
.info-site b{font-size:25px;font-weight:500}
</style>
</head>
<body>
<div class="canvas">

  <section class="page front">
    <header class="header">
      <div class="header-strip"></div>
      <p class="ages">ALL AGES<br>WELCOME</p>
      <span class="brand-left">VORDO</span>
      <span class="brand-seal"></span>
      <span class="brand-right">DUBAI</span>
    </header>
    <div class="rule-yellow" style="top:157px"></div>

    <div class="hero-photo" role="img" aria-label="Athletic woman in black sportswear holding dumbbells, looking over her shoulder"></div>

    <h1 class="title">GRAND OPENING</h1>
    <div class="title-rule"></div>
    <p class="date">SATURDAY 10<sup>TH</sup> FEBRUARY</p>
    <div class="date-rule"></div>

    <div class="timetable-head">GRAND OPENING TIMETABLE</div>
    <div class="timeline"></div>
    <div class="slot" style="top:358px"><span class="time">10 AM</span>GYM Opening</div>
    <div class="slot" style="top:388px"><span class="time">11 AM</span>Power PGU</div>
    <div class="slot" style="top:418px"><span class="time">01 PM</span>Body GT</div>
    <div class="slot" style="top:449px"><span class="time">03 PM</span>Calone Bum</div>
    <div class="slot" style="top:479px"><span class="time">07 PM</span>GYM Closing</div>

    <div class="offer-band"></div>
    <div class="offer-label">SPEICAL<br>OFFER</div>
    <p class="offer-text">Show this flyer and entitle to get THREE(3) free classes. This offer valid only till March 10, 2018.</p>

    <h2 class="about-head">About Vordo Fitness</h2>
    <p class="about-text">Vordo Fitness is a gym focused on circuit style training for all levels of fitness. We provide engaging and motivating group exercise classes that are both challanging and fun.</p>
    <p class="call">CALL : 01 555 01234</p>
  </section>

  <section class="page back">
    <div class="photo" style="left:0;width:186px;background:linear-gradient(160deg,#8a7a6c,#3f3a36)" role="img" aria-label="Group of people lying in a circle doing a floor exercise"></div>
    <div class="photo" style="left:188px;width:188px;background:radial-gradient(circle at 50% 55%,#2a2c2a 30%,#6f6a66 70%,#9a8f88)" role="img" aria-label="Kettlebell on the floor beside a resting athlete"></div>
    <div class="photo" style="left:378px;width:54px;background:linear-gradient(180deg,#7a4a48,#3a3636)" role="img" aria-label="Small collage of studio training shots"></div>
    <div class="photo" style="left:434px;width:106px;height:78px;background:linear-gradient(180deg,#b8b6b0,#4a4846)" role="img" aria-label="Battle rope training in a bright studio"></div>
    <div class="photo" style="left:434px;top:81px;width:106px;height:82px;background:linear-gradient(180deg,#9c9a96,#3e3c3a)" role="img" aria-label="Partner workout by the studio windows"></div>
    <div class="rule-yellow" style="top:163px"></div>

    <div class="scene" role="img" aria-label="Man training with a kettlebell on a rooftop terrace overlooking the city skyline"></div>

    <h2 class="facilities-head">OUR FACILITIES</h2>
    <div class="pill" style="top:239px">INDOOR STUDIO</div>
    <p class="desc" style="top:268px">The indoor studio has a bright open space for functional training.</p>
    <div class="pill" style="top:321px">OUTDOOR TERRACE</div>
    <p class="desc" style="top:350px">Our 2000 ft² outdoor terrace boost panoramic views over Dubai's most prominent landmarks and will make you want to push that extra repetition.</p>
    <div class="pill" style="top:432px">LOCKER ROOMS</div>
    <p class="desc" style="top:461px">Changing facilities with lockers, shower and sauna.</p>
    <div class="pill" style="top:513px">LOUNGE AREA</div>
    <p class="desc" style="top:541px">The outdoor terrace also features a lounge area for relaxing after a hard workout.</p>

    <p class="follow">FOLLOW US ON</p>
    <div class="social social-a"><span class="mark"></span>/ vordofit</div>
    <div class="social social-b"><span class="mark"></span>/ vordofit</div>

    <div class="info-band">
      <p class="info-links">CLASSES &nbsp;•&nbsp; TIME TABLES &nbsp;•&nbsp; PRICING</p>
      <p class="info-site">check more info on <b>www.vordo.example</b></p>
    </div>
  </section>

</div>
</body>
</html>
```